the theater production needs a poster design

we need a poster design for a theater drama in Seoul , South Korea.

the title : THE LANTERN KEEPER'S ROAD
BASED ON WALTER DREVICK'S BOOK

where:Haneulbit Stagehouse, Jongro-Gu, Seoul
when:2022.1.1~OpenRun
Saturday 3PM, 63PM, Sunday 5pm, Monday 7:30pm

TICKET PRICE: $45

BOOK NOW
02 471 6039
RIVA TROUPE

Director Minha Park Composer Sora Lee, Sound Director Doyun Han
Producer Taesik Yoon

Target Market(s)

for Chiristan and others

Industry/Entity Type

Christian community and non Christian society

Colors
0094D4
00A9DD
6FCCEA
C7EBF8
E9F6FB

Requirements
Must have
• the main Character, pilgrim should should carry some burdens on his shoulder

```html
<!DOCTYPE html>
<html lang="en">
<head>
<meta charset="utf-8">
<title>The Lantern Keeper's Road — Theatre Poster</title>
<link rel="stylesheet" href="https://fonts.googleapis.com/css2?family=Oswald:wght@400;500;600;700&family=Rubik+Dirt&display=swap">
<style>
  :root {
    --blue-deep: #0094D4;
    --blue-mid: #00A9DD;
    --blue-soft: #6FCCEA;
    --blue-mist: #C7EBF8;
    --blue-pale: #E9F6FB;
    --ink-dark: #05080a;
    --sky-warm: #a98f86;
    --hill-shade: #3c3d3a;
    --ground: #181716;
    --figure-tone: #4a4a3f;
    --figure-edge: #2c2b25;
    --text-light: #f1efec;
    --text-soft: #e2ded9;
    --band-red: #d0202a;
    --price-pink: rgba(214, 120, 118, 0.85);
  }
  * { margin: 0; padding: 0; box-sizing: border-box; }
  html, body {
    width: 848px;
    height: 1200px;
    overflow: hidden;
    background: var(--ink-dark);
  }
  .poster {
    position: relative;
    width: 848px;
    height: 1200px;
    overflow: hidden;
    font-family: "Oswald", sans-serif;
    color: var(--text-light);
  }
  .poster__landscape {
    position: absolute;
    inset: 0;
    background:
      radial-gradient(ellipse 70% 30% at 60% 40%, rgba(199,235,248,0.28), transparent 70%),
      radial-gradient(ellipse 60% 25% at 80% 52%, rgba(0,148,212,0.22), transparent 70%),
      linear-gradient(180deg, var(--sky-warm) 0%, #8a8583 24%, #6f7a80 38%, var(--hill-shade) 56%, var(--ground) 76%, var(--ink-dark) 100%);
  }
  .poster__pilgrim {
    position: absolute;
    left: 300px;
    top: 250px;
    width: 340px;
    height: 560px;
    border-radius: 46% 46% 18% 18% / 30% 30% 10% 10%;
    background:
      radial-gradient(ellipse 55% 12% at 50% 8%, rgba(90,80,70,0.95), transparent 100%),
      radial-gradient(ellipse 28% 14% at 60% 58%, rgba(110,85,60,0.9), transparent 100%),
      linear-gradient(180deg, var(--figure-tone) 0%, var(--figure-edge) 100%);
    opacity: 0.9;
  }
  .credits {
    position: absolute;
    top: 86px;
    right: 48px;
    text-align: right;
    text-transform: uppercase;
    letter-spacing: 1.5px;
    line-height: 1.35;
  }
  .credits__row { font-size: 22px; font-weight: 600; }
  .credits__role { font-size: 12px; font-weight: 500; margin: 0 4px; color: var(--text-soft); }
  .price {
    position: absolute;
    top: 262px;
    left: 72px;
    width: 140px;
    height: 140px;
    border-radius: 50%;
    background: var(--price-pink);
    display: flex;
    flex-direction: column;
    align-items: center;
    justify-content: center;
  }
  .price__label { font-size: 15px; font-weight: 500; }
  .price__amount { font-size: 42px; font-weight: 700; line-height: 1; }
  .source-band {
    position: absolute;
    top: 640px;
    left: 50%;
    transform: translateX(-40%);
    background: var(--band-red);
    padding: 7px 22px;
    font-size: 21px;
    font-weight: 600;
    letter-spacing: 2px;
    text-transform: uppercase;
    white-space: nowrap;
  }
  .title {
    position: absolute;
    top: 694px;
    left: 0;
    right: 0;
    text-align: center;
    font-family: "Rubik Dirt", "Oswald", sans-serif;
    font-weight: 400;
    font-size: 92px;
    line-height: 0.98;
    color: var(--text-light);
    text-transform: uppercase;
  }
  .info {
    position: absolute;
    left: 48px;
    right: 48px;
    bottom: 56px;
    display: flex;
    justify-content: space-between;
    align-items: flex-start;
    text-transform: uppercase;
    font-size: 16px;
    font-weight: 500;
    letter-spacing: 2.5px;
    line-height: 1.6;
  }
  .info__times { text-align: center; }
  .info__booking { text-align: right; }
  .info__booking-title { color: var(--blue-mist); }
</style>
</head>
<body>
  <main class="poster">
    <div class="poster__landscape" role="img" aria-label="Misty autumn mountains at dusk above a valley village, with orange trees and a blue haze in the distance"></div>
    <div class="poster__pilgrim" role="img" aria-label="The pilgrim seen from behind in a wide conical straw hat and long robe, a heavy burden bag strapped over his shoulder and a staff in hand"></div>

    <header class="credits">
      <p class="credits__row"><span class="credits__role">Director</span>Minha Park<span class="credits__role">Composer</span>Sora Lee</p>
      <p class="credits__row"><span class="credits__role">Sound Director</span>Doyun Han<span class="credits__role">Producer</span>Taesik Yoon</p>
    </header>

    <div class="price">
      <span class="price__label">HTM</span>
      <span class="price__amount">$45</span>
    </div>

    <p class="source-band">Based on Walter Drevick's Book</p>

    <h1 class="title">The Lantern<br>Keeper's Road</h1>

    <footer class="info">
      <div class="info__venue">Haneulbit Stagehouse,<br>Jongro-Gu, Seoul</div>
      <div class="info__dates">2022.01.01<br>~OpenRun</div>
      <div class="info__times">Saturday : 3PM, 6PM<br>Sunday : 5PM<br>Monday : 7.30 PM</div>
      <div class="info__booking"><span class="info__booking-title">Book Now</span><br>02 471 6039<br>Riva Troupe</div>
    </footer>
  </main>
</body>
</html>
```